Kessler MD Summit Primary Care Business Card

Need a business card for a medical clinic targeting VIP patients. Should portray an upscale feeling. Simple, clean design. Logo and colors need to be incorporated into card. Clinic colors are gray/ silver, blues, white same as logo.
Clinic is a cash only VIP service clinic targeting higher income patients.
Tagline: "Where every visit feels personal - Care Without Rush"

Target Market(s)

VIP, upscale

Industry/Entity Type

Medical

Contact Information for Business Card

Would like to use for cards with raised print or metallic highlight.

Requirements
Must have
• Incorporate logo, Use colors in logo
Nice to have
• Metallic detail
Should not have
• too much details or colors, other stock photos or designs

```html
<!DOCTYPE html>
<html lang="en">
<head>
<meta charset="utf-8">
<title>Kessler MD Summit Primary Care – Business Card</title>
<link rel="stylesheet" href="https://fonts.googleapis.com/css2?family=Open+Sans:wght@400;600&display=swap">
<style>
  :root {
    --backdrop: #e8e5e1;
    --card-white: #ffffff;
    --navy: #34475b;
    --slate: #3f5064;
    --band: #3d4f62;
    --gray-text: #7d7f82;
    --silver: #a9adb2;
    --divider: #9a9ca0;
  }
  * { margin: 0; padding: 0; box-sizing: border-box; }
  html, body { width: 1200px; height: 1000px; overflow: hidden; }
  body {
    background: var(--backdrop);
    font-family: "Open Sans", Arial, sans-serif;
    position: relative;
  }
  .card {
    position: absolute;
    left: 266px;
    width: 666px;
    height: 396px;
  }
  .card-front { top: 74px; background: var(--card-white); }
  .card-back { top: 534px; background: var(--slate); }

  .brand-mark {
    position: absolute;
    border-radius: 50%;
  }
  .brand-name {
    position: absolute;
    text-align: center;
    font-weight: 400;
    letter-spacing: 1px;
    line-height: 1.2;
  }
  .card-front .brand-mark {
    left: 142px; top: 110px; width: 80px; height: 80px;
    background: var(--silver);
  }
  .card-front .brand-name {
    left: 30px; width: 304px; top: 226px;
    font-size: 23px;
    color: var(--navy);
  }

  .divider {
    position: absolute;
    left: 352px; top: 89px;
    width: 2px; height: 191px;
    background: var(--divider);
  }
  .contact {
    position: absolute;
    left: 382px; top: 84px;
    color: var(--gray-text);
    font-size: 16px;
  }
  .person-name {
    font-size: 21px; font-weight: 600;
    color: var(--navy);
    letter-spacing: 0.3px;
    line-height: 26px;
  }
  .person-role { font-size: 16.5px; line-height: 20px; }
  .address { margin-top: 10px; font-size: 16.5px; line-height: 21px; }
  .contact-list { list-style: none; margin-top: 8px; }
  .contact-list li {
    display: flex; align-items: center; gap: 8px;
    line-height: 22px; font-size: 16.5px;
  }
  .contact-list svg { width: 14px; height: 14px; fill: var(--navy); flex: none; }

  .tagline-band {
    position: absolute;
    left: 0; top: 342px; width: 100%; height: 35px;
    background: var(--band);
    color: #ffffff;
    font-size: 16.5px;
    text-align: center;
    line-height: 35px;
  }

  .card-back .brand-mark {
    left: 283px; top: 90px; width: 100px; height: 100px;
    background: var(--silver);
  }
  .card-back .brand-name {
    left: 0; width: 100%; top: 250px;
    font-size: 30px;
    color: var(--silver);
  }
</style>
</head>
<body>
  <section class="card card-front" aria-label="Business card front">
    <div class="brand-mark"></div>
    <div class="brand-name">KESSLER MD<br>SUMMIT PRIMARY CARE</div>

    <div class="divider"></div>

    <div class="contact">
      <div class="person-name">MAREN HOLLOWAY</div>
      <div class="person-role">Managing Director</div>
      <div class="address">Ashcombe Lane, Brindley,<br>Wessex, BX4 2QT</div>
      <ul class="contact-list">
        <li>
          <svg viewBox="0 0 16 16" aria-hidden="true"><path d="M1 5c0-2 3-3 7-3s7 1 7 3v1h-3.5V4.5h-7V6H1z M3 7h10l1.5 7h-13z M6 9h4v3H6z"/></svg>
          + 000 000 0000
        </li>
        <li>
          <svg viewBox="0 0 16 16" aria-hidden="true"><path d="M4 1h8v4H4z M1 6h14v6h-3v3H4v-3H1z M5 10v4h6v-4z"/></svg>
          + 000 000 0000
        </li>
        <li>
          <svg viewBox="0 0 16 16" aria-hidden="true"><path d="M1 3h14v10H1z M2 4v1l6 4 6-4V4z" fill-rule="evenodd"/></svg>
          info@kesslermdsummitpc.com
        </li>
        <li>
          <svg viewBox="0 0 16 16" aria-hidden="true"><path d="M8 1a7 7 0 1 0 0 14A7 7 0 0 0 8 1zm0 1.6a5.4 5.4 0 0 1 0 10.8A5.4 5.4 0 0 1 8 2.6zM4 7h8v2H4z M7 4h2v8H7z"/></svg>
          www.kesslermdsummitpc.com
        </li>
      </ul>
    </div>

    <div class="tagline-band">Where every visit feels personal - Care Without Rush</div>
  </section>

  <section class="card card-back" aria-label="Business card back">
    <div class="brand-mark"></div>
    <div class="brand-name">KESSLER MD<br>SUMMIT PRIMARY CARE</div>
  </section>
</body>
</html>
```